Client Meeting and installation Email Follow up

I would like a follow-up email template created.
Currently, we do a lot of new construction builds and meet with clients about 6-3 months before they take possession of their new house. I want a follow-up email template to be sent after the homeowner takes possession of their house that enquires if the clients are happy about their new lighting, the service they received, and their customer service representative with Meridale Glow and Breeze. I have attached a few files of what our current marketing looks like.
Target Market(s)
Home Owners We have already met with
Industry/Entity Type
Residential lighting
Font styles to use
Other font styles liked:
- Alta Light, Playfair Display, Montserrat
Colors
Designer to choose colors to be used in the design.
Look and feel
Each slider illustrates characteristics of the customer's brand and the style your logo design should communicate.

```html
<!DOCTYPE html>
<html lang="en">
<head>
<meta charset="utf-8">
<title>How's Your New Home Looking? – Meridale Glow and Breeze</title>
<link href="https://fonts.googleapis.com/css2?family=Montserrat:ital,wght@0,400;0,600;0,700;1,600&family=Playfair+Display:ital,wght@1,400;1,500&display=swap" rel="stylesheet">
<style>
  :root {
    --ink: #0d0d0d;
    --paper: #ffffff;
    --mist: #f3f4f3;
    --blush: #d9b8a2;
    --blush-band: #ecdcd3;
    --sand-light: #f1ece4;
    --sand-mid: #ddd2c2;
    --marble-a: #eef0f0;
    --marble-b: #dfe2e3;
  }
  * { box-sizing: border-box; margin: 0; padding: 0; }
  html, body { width: 765px; height: 1200px; overflow: hidden; background: var(--paper); }
  .email {
    position: relative;
    width: 765px;
    height: 1200px;
    overflow: hidden;
    font-family: "Montserrat", sans-serif;
    color: var(--ink);
  }
  .hero-photo {
    position: absolute; left: 0; top: 0; width: 765px; height: 181px;
    background: linear-gradient(100deg, var(--sand-light) 0%, #e9e1d5 30%, #f6f4f1 55%, var(--sand-mid) 80%, #eceae6 100%);
  }
  .brand-plate {
    position: absolute; left: 197px; top: 23px; width: 365px; height: 120px;
    background: var(--paper);
    display: flex; align-items: center; justify-content: center;
  }
  .brand-name {
    font-family: "Montserrat", sans-serif;
    font-weight: 600;
    font-size: 24px;
    letter-spacing: 0.5px;
    color: var(--ink);
  }
  .headline {
    position: absolute; left: 146px; top: 205px; width: 520px;
    font-family: "Playfair Display", serif;
    font-style: italic;
    font-weight: 400;
    font-size: 68px;
    line-height: 82px;
  }
  .letter {
    position: absolute; left: 0; top: 405px; width: 765px; height: 710px;
    background: var(--mist);
  }
  .greeting {
    position: absolute; left: 147px; top: 16px;
    font-weight: 700; font-size: 16px;
  }
  .body-copy {
    position: absolute; left: 147px; width: 473px;
    font-size: 16.5px; line-height: 21.5px; text-align: justify;
  }
  .intro-1 { top: 56px; }
  .intro-2 { top: 120px; }
  .question {
    position: absolute; left: 140px; width: 480px; height: 80px;
  }
  .question-number {
    position: absolute; left: 0; top: 0; width: 80px; height: 80px;
    border-radius: 50%; background: var(--blush);
    display: flex; align-items: center; justify-content: center;
    font-family: "Playfair Display", serif; font-style: italic; font-weight: 500;
    font-size: 56px; line-height: 1;
  }
  .question-text {
    position: absolute; left: 97px; width: 375px;
    font-style: italic; font-weight: 600;
    font-size: 15.5px; line-height: 20px; text-align: justify;
  }
  .q1 { top: 236px; } .q1 .question-text { top: 14px; }
  .q2 { top: 344px; } .q2 .question-text { top: 14px; left: 102px; width: 370px; }
  .q3 { top: 445px; } .q3 .question-text { top: 17px; text-align: left; }
  .closing { left: 139px; width: 475px; text-align: left; }
  .closing-1 { top: 562px; }
  .closing-2 { top: 626px; }
  .marble-footer {
    position: absolute; left: 0; top: 1115px; width: 765px; height: 85px;
    background: linear-gradient(120deg, var(--marble-a) 0%, var(--marble-b) 35%, #f4f5f5 60%, var(--marble-b) 100%);
  }
  .footer-band {
    position: absolute; left: 0; top: 37px; width: 765px; height: 16px;
    background: var(--blush-band);
  }
</style>
</head>
<body>
<main class="email">
  <div class="hero-photo" role="img" aria-label="Photo of a bright living space with a macramé hammock chair, woven basket and tasselled throw"></div>
  <div class="brand-plate"><span class="brand-name">Meridale Glow and Breeze</span></div>

  <h1 class="headline">How’s Your New Home Looking?</h1>

  <section class="letter">
    <p class="greeting">Hi [Client's First Name]</p>
    <p class="body-copy intro-1">I hope this message finds you well and that you’re settling into your new home comfortably.</p>
    <p class="body-copy intro-2">We genuinely value your feedback and would love to hear about your experience with Meridale Glow and Breeze. If you have a moment, could you share your thoughts on the following:</p>

    <div class="question q1">
      <span class="question-number">1</span>
      <p class="question-text">Are you satisfied with the lighting in your new home? Is there anything you’d like to change or add?</p>
    </div>
    <div class="question q2">
      <span class="question-number">2</span>
      <p class="question-text">How was your overall experience with our service? Were there any areas where we could improve?</p>
    </div>
    <div class="question q3">
      <span class="question-number">3</span>
      <p class="question-text">How did you find working with our representative? Did they meet your expectations?</p>
    </div>

    <p class="body-copy closing closing-1">Your input is important to us, please feel free to reply to this email with any comments or suggestions.</p>
    <p class="body-copy closing closing-2">Thank you for choosing Meridale Glow and Breeze. If you need any further assistance, we’re always here to help.</p>
  </section>

  <footer class="marble-footer" role="img" aria-label="Soft white marble texture">
    <div class="footer-band"></div>
  </footer>
</main>
</body>
</html>
```